Create Premium Wine Label Design

We are premium wine exporters from Australia. We are looking to introduce new brand " The Velloro" - in red wine, White wine and Sparkling wine to international market.

The sample label design for red wine ( Shiraz) is attached.

This is our luxury brand. We need a stunning wine label designs for (front, back and neck) that should be mostly in GOLD colour and design should be really eye catching.

We have provided sample design for front, back and neck labels. However, we are looking forward to see a completely new improvised design.

LOGO attached.

Front Label Design Specification:

* We would like to see designs that are in Gold colour.
* Wine Bottle size is standard: 750ml; we assume the same design can be resizable to different bottle sizes.
* Our design should suit both black, white and sparkling wine bottles(sample attached)
* Use our logo in the design (see attached - label sample)
* Content for front label (see attached).
* Design should include all information specified in the sample

Back Label Design
* All contents in the sample should be used ( sample attached)
* LOGO attached.

Neck Label Design
* Sample of Neck label attached, please provide similar or your own design.
* LOGO attached.

Image Samples:
* Samples of label designs we like (see attached)
* Sample for gold color (see attached)
* For bottle shapes (see attached)
* Front, Back and Neck Label Samples (see attached)

Target Market(s)

International Wine Market

Font styles to use
Decorative
Script

Requirements
Must have
• Must have golden color on front and back label

```html
<!DOCTYPE html>
<html lang="en">
<head>
<meta charset="utf-8">
<title>The Velloro Shiraz – Label</title>
<link href="https://fonts.googleapis.com/css2?family=Cormorant+Garamond:ital,wght@0,500;0,600;1,500&family=Montserrat:wght@400;500&display=swap" rel="stylesheet">
<style>
  :root {
    --paper: #f4f3f1;
    --label-black: #1c1c1d;
    --label-charcoal: #3a3a3c;
    --gold: #d4ad57;
    --gold-light: #f1dc9a;
    --gold-deep: #a9802f;
    --gold-dim: #6e5629;
    --cream: #efe3c4;
    --ink: #1a1a1a;
  }
  * { margin: 0; padding: 0; box-sizing: border-box; }
  html, body {
    width: 1200px;
    height: 3068px;
    overflow: hidden;
    background: var(--paper);
  }
  .canvas {
    position: relative;
    width: 1200px;
    height: 3068px;
  }

  /* Neck label */
  .neck-label {
    position: absolute;
    left: 250px;
    top: 470px;
    width: 700px;
    height: 120px;
    background: var(--label-black);
    display: flex;
    align-items: center;
    justify-content: center;
  }
  .neck-label::before,
  .neck-label::after {
    content: "";
    position: absolute;
    left: 0;
    right: 0;
    height: 6px;
    background: linear-gradient(90deg, var(--gold-deep), var(--gold-light), var(--gold-deep));
  }
  .neck-label::before { top: 14px; }
  .neck-label::after { bottom: 14px; }
  .neck-name {
    font-family: "Cormorant Garamond", serif;
    font-weight: 600;
    font-size: 44px;
    letter-spacing: 6px;
    color: var(--gold);
    text-transform: uppercase;
  }

  /* Front label */
  .front-label {
    position: absolute;
    left: 190px;
    top: 760px;
    width: 820px;
    height: 1580px;
    overflow: hidden;
    background: var(--label-black);
  }

  /* Gold line-pattern zone along the edges and above the gold band */
  .pattern-zone {
    position: absolute;
    inset: 0 0 350px 0;
    background:
      linear-gradient(180deg, rgba(212,173,87,0.55) 0%, rgba(212,173,87,0.18) 12%, rgba(212,173,87,0) 22%, rgba(212,173,87,0) 78%, rgba(212,173,87,0.35) 92%, rgba(241,220,154,0.6) 100%),
      linear-gradient(90deg, var(--gold-deep) 0%, var(--gold-dim) 9%, var(--label-black) 18%, var(--label-black) 82%, var(--gold-dim) 91%, var(--gold-deep) 100%);
  }
  .label-field {
    position: absolute;
    left: 150px;
    right: 150px;
    top: 170px;
    bottom: 560px;
    border-radius: 40px;
    background: radial-gradient(ellipse at 50% 40%, var(--label-charcoal) 0%, var(--label-black) 80%);
    box-shadow: 0 0 80px 60px var(--label-black);
  }

  .brand {
    position: absolute;
    top: 420px;
    left: 0;
    right: 0;
    display: flex;
    align-items: center;
    justify-content: center;
    gap: 18px;
  }
  .brand-dot {
    width: 26px;
    height: 26px;
    border-radius: 50%;
    background: var(--gold);
  }
  .brand-name {
    font-family: "Cormorant Garamond", serif;
    font-weight: 600;
    font-size: 58px;
    letter-spacing: 4px;
    color: var(--gold);
    text-transform: uppercase;
  }
  .varietal {
    position: absolute;
    top: 680px;
    left: 0;
    right: 0;
    text-align: center;
    font-family: "Cormorant Garamond", serif;
    font-weight: 500;
    font-size: 72px;
    letter-spacing: 16px;
    color: var(--cream);
  }

  .gold-band {
    position: absolute;
    left: 0;
    right: 0;
    bottom: 0;
    height: 350px;
    background: linear-gradient(100deg, var(--gold-deep) 0%, var(--gold-light) 35%, var(--gold) 60%, var(--gold-light) 85%, var(--gold-deep) 100%);
    text-align: center;
    color: var(--ink);
  }
  .wine-name {
    position: absolute;
    top: 40px;
    left: 0;
    right: 0;
    font-family: "Cormorant Garamond", serif;
    font-style: italic;
    font-weight: 500;
    font-size: 78px;
  }
  .vintage {
    position: absolute;
    top: 170px;
    left: 0;
    right: 0;
    font-family: "Montserrat", sans-serif;
    font-weight: 500;
    font-size: 52px;
    letter-spacing: 3px;
  }
  .origin {
    position: absolute;
    top: 280px;
    left: 0;
    right: 0;
    font-family: "Montserrat", sans-serif;
    font-weight: 400;
    font-size: 24px;
    letter-spacing: 5px;
    color: #4a3c20;
  }
</style>
</head>
<body>
  <main class="canvas">
    <section class="neck-label">
      <span class="neck-name">Southvale</span>
    </section>

    <section class="front-label">
      <div class="pattern-zone" role="img" aria-label="Thin gold geometric line pattern radiating along the label edges and above the gold band"></div>
      <div class="label-field"></div>

      <div class="brand">
        <span class="brand-dot"></span>
        <span class="brand-name">Southvale</span>
      </div>

      <h1 class="varietal">SHIRAZ</h1>

      <div class="gold-band">
        <p class="wine-name">The Velloro</p>
        <p class="vintage">2018</p>
        <p class="origin">WINE OF AUSTRALIA</p>
      </div>
    </section>
  </main>
</body>
</html>
```